Business Card Design for Loft Pictures

Hi we need a business card designed for a new aerial photography business we have started, we use UAV Drones to take photos for corporate, events, real estate, local government etc , the business name is Loft Pictures Australia, we have a facebook page that might help you come up with some designs - https://www.facebook.com/loftpicturesaustralia

We need to have and editable AI file so that we can use different names and contact details. details for one of the cards as follow:

Ned Harrow
phone: 03 5521 4736
Mobile: 0431 957 284
email: ned@loftpicturez.example
web: www.loftpictures.example

have now changed: Designer Payment:Committed

Target Market(s)

We are a Aerial Photography business using Drones and UAV

Industry/Entity Type

Business

Logo Text

Loft Pictures Australia

Requirements
Must have
• Colors to match logo and be part of Loft Pictures Brand

```html
<!DOCTYPE html>
<html lang="en">
<head>
<meta charset="utf-8">
<title>Loft Pictures Australia – Business Card</title>
<link rel="stylesheet" href="https://fonts.googleapis.com/css2?family=Lato:wght@700;900&family=Roboto+Condensed:wght@400&display=swap">
<style>
  :root {
    --backdrop: #3a3a3c;
    --card: #ffffff;
    --ink: #1f1f1f;
    --brand-grey: #2b2b2b;
    --teal: #45b5c4;
    --teal-dark: #3aa7b7;
    --sky-top: #c9ced4;
    --sky-mid: #8e9aa5;
    --ground: #6b7a58;
  }
  * { box-sizing: border-box; margin: 0; padding: 0; }
  html, body { width: 1200px; height: 1200px; overflow: hidden; }
  body { background: var(--backdrop); position: relative; font-family: "Roboto Condensed", "Arial Narrow", sans-serif; }

  .card { position: absolute; background: var(--card); }

  /* Front */
  .card-front { left: 49px; top: 10px; width: 1054px; height: 598px; }
  .front-brand {
    position: absolute; left: 0; right: 0; top: 60px; text-align: center;
    font-family: "Lato", sans-serif; font-weight: 900; color: var(--brand-grey);
    text-transform: uppercase; line-height: 1;
  }
  .front-brand .brand-line-1 { display: block; font-size: 112px; letter-spacing: 2px; }
  .front-brand .brand-line-2 { display: block; font-size: 40px; letter-spacing: 22px; margin-top: 34px; padding-left: 22px; }
  .front-photo {
    position: absolute; left: 362px; top: 348px; width: 375px; height: 179px;
    background: linear-gradient(180deg, var(--sky-top) 0%, var(--sky-mid) 38%, var(--ground) 62%, #8a8f93 100%);
  }
  .front-web {
    position: absolute; left: 0; right: 0; top: 530px; text-align: center;
    font-size: 29px; color: var(--ink); padding-right: 80px;
  }

  /* Back */
  .card-back { left: 84px; top: 587px; width: 1050px; height: 598px; }
  .person { position: absolute; left: 90px; top: 138px; }
  .person-name { font-family: "Lato", sans-serif; font-weight: 700; font-size: 34px; color: var(--teal); line-height: 1; }
  .person-role { font-size: 29px; color: var(--ink); margin-top: 6px; }

  .contacts { position: absolute; left: 86px; top: 266px; list-style: none; }
  .contacts li { display: flex; align-items: center; height: 40.5px; font-size: 30px; color: var(--ink); }
  .contacts svg { width: 28px; height: 28px; margin-right: 22px; flex: none; }

  .back-brand {
    position: absolute; left: 620px; top: 160px; width: 340px; text-align: center;
    font-family: "Lato", sans-serif; font-weight: 900; color: var(--brand-grey);
    text-transform: uppercase; line-height: 1;
  }
  .back-brand .brand-line-1 { display: block; font-size: 56px; }
  .back-brand .brand-line-2 { display: block; font-size: 22px; letter-spacing: 10px; margin-top: 22px; padding-left: 10px; }

  .tagline-band {
    position: absolute; left: 0; right: 0; bottom: 0; height: 125px; background: var(--teal);
    display: flex; align-items: center; justify-content: center;
    font-family: "Lato", sans-serif; font-weight: 700; font-size: 36px; letter-spacing: 7px; color: #fff;
    padding-bottom: 10px; padding-left: 20px;
  }
</style>
</head>
<body>
  <section class="card card-front">
    <div class="front-brand">
      <span class="brand-line-1">Loft Pictures</span>
      <span class="brand-line-2">Australia</span>
    </div>
    <div class="front-photo" role="img" aria-label="Aerial photograph of a city skyline beyond a road, buildings and parkland"></div>
    <p class="front-web">www.loftpictures.example</p>
  </section>

  <section class="card card-back">
    <div class="person">
      <p class="person-name">Ned Harrow</p>
      <p class="person-role">Aerial Photographer</p>
    </div>

    <ul class="contacts">
      <li>
        <svg viewBox="0 0 28 28" aria-hidden="true"><circle cx="14" cy="14" r="14" fill="var(--teal)"/><path d="M7 12c0-3 14-3 14 0v2h-4v-2H11v2H7z M9 15h10l1 5H8z" fill="#fff"/></svg>
        03 5521 4736
      </li>
      <li>
        <svg viewBox="0 0 28 28" aria-hidden="true"><rect x="7" y="2" width="14" height="24" rx="2" fill="var(--teal)"/><rect x="9.5" y="6" width="9" height="13" fill="#fff"/><circle cx="14" cy="22.5" r="1.5" fill="#fff"/></svg>
        0431 957 284
      </li>
      <li>
        <svg viewBox="0 0 28 28" aria-hidden="true"><circle cx="14" cy="14" r="14" fill="var(--teal)"/><rect x="7" y="9" width="14" height="10" fill="#fff"/><path d="M7 9l7 6 7-6" stroke="var(--teal)" stroke-width="1.5" fill="none"/></svg>
        ned@loftpicturez.example
      </li>
      <li>
        <svg viewBox="0 0 28 28" aria-hidden="true"><circle cx="14" cy="14" r="14" fill="var(--teal)"/><g stroke="#fff" stroke-width="1.6" fill="none"><circle cx="14" cy="14" r="8"/><ellipse cx="14" cy="14" rx="3.5" ry="8"/><path d="M6 14h16M8 10h12M8 18h12"/></g></svg>
        www.loftpictures.example
      </li>
    </ul>

    <div class="back-brand">
      <span class="brand-line-1">Loft Pictures</span>
      <span class="brand-line-2">Australia</span>
    </div>

    <div class="tagline-band">Professional Aerial Photography</div>
  </section>
</body>
</html>
```